Aunt Rolina's Bakery

I am about to create a luxury boutique that specializes in cake baking and cupcake
and ready for parties and special events and order delivery
the logo has already made

Industry/Entity Type

Boutique

Contact Information for Business Card

Email:auntrolinasbakery@maplecrumbmail.com
Instagram: aunt_rolina_bakery
Twitter: xxxxxxx
WhatsApp: xxxxxxx

Requirements
Must have
• luxury design

```html
<!DOCTYPE html>
<html lang="en">
<head>
<meta charset="UTF-8">
<title>Aunt Rolina's Bakery – Business Card</title>
<link href="https://fonts.googleapis.com/css2?family=Lato:wght@400;700&display=swap" rel="stylesheet">
<style>
  :root {
    --page-bg: #e9e6e3;
    --card-black: #1b1b1c;
    --card-black-soft: #262627;
    --rose: #e19aae;
    --text-light: #f2f2f2;
  }
  * { margin: 0; padding: 0; box-sizing: border-box; }
  html, body {
    width: 1200px;
    height: 844px;
    overflow: hidden;
    background: var(--page-bg);
    font-family: "Lato", sans-serif;
  }
  .card-set {
    position: relative;
    width: 1200px;
    height: 844px;
  }
  .card {
    position: absolute;
    top: 272px;
    width: 520px;
    height: 300px;
    background: linear-gradient(135deg, var(--card-black) 60%, var(--card-black-soft));
    box-shadow: 0 8px 22px rgba(0,0,0,0.22);
    overflow: hidden;
  }
  .card--contact { left: 50px; }
  .card--brand { left: 630px; }

  /* contact side */
  .band {
    position: absolute;
    left: 0;
    width: 100%;
    height: 11px;
    background: var(--rose);
  }
  .band--top { top: 0; }
  .band--bottom { bottom: 0; }

  .person {
    position: absolute;
    top: 56px;
    left: 0;
    width: 100%;
    text-align: center;
  }
  .person__name {
    display: inline-block;
    color: var(--rose);
    font-size: 17px;
    font-weight: 400;
    letter-spacing: 0.5px;
    text-transform: uppercase;
    padding-bottom: 3px;
    border-bottom: 1.5px solid var(--rose);
  }
  .person__role {
    color: var(--text-light);
    font-size: 13px;
    margin-top: 3px;
  }

  .contact-list {
    position: absolute;
    top: 140px;
    left: 0;
    width: 100%;
    list-style: none;
    text-align: center;
  }
  .contact-list__item {
    color: var(--text-light);
    font-size: 13px;
    line-height: 19px;
  }
  .contact-list__icon {
    display: inline-block;
    width: 10px;
    height: 10px;
    margin-right: 5px;
    vertical-align: -1px;
  }
  .contact-list__mark {
    display: inline-block;
    width: 9px;
    height: 9px;
    margin-right: 6px;
    background: var(--rose);
    border-radius: 2px;
    vertical-align: 0;
  }
  .address {
    position: absolute;
    bottom: 30px;
    left: 0;
    width: 100%;
    text-align: center;
    color: var(--text-light);
    font-size: 14px;
  }

  /* brand side */
  .tab {
    position: absolute;
    width: 16px;
    height: 34px;
    background: var(--rose);
  }
  .tab--right { right: 0; top: 40px; }
  .tab--left { left: 0; top: 190px; }

  .brand {
    position: absolute;
    top: 0;
    left: 0;
    width: 100%;
    height: 100%;
    display: flex;
    align-items: center;
    justify-content: center;
  }
  .brand__name {
    color: var(--text-light);
    font-size: 26px;
    font-weight: 400;
    letter-spacing: 1px;
  }
</style>
</head>
<body>
  <main class="card-set">
    <section class="card card--contact" aria-label="Contact side">
      <div class="band band--top"></div>
      <div class="person">
        <div class="person__name">Daniel Hartley</div>
        <div class="person__role">Managing Director</div>
      </div>
      <ul class="contact-list">
        <li class="contact-list__item">
          <svg class="contact-list__icon" viewBox="0 0 10 10" aria-hidden="true">
            <rect x="0.5" y="1.5" width="9" height="7" fill="var(--rose)"/>
            <path d="M0.5 1.8 L5 5.5 L9.5 1.8" stroke="var(--card-black)" stroke-width="1" fill="none"/>
          </svg>auntrolinasbakery@maplecrumbmail.com
        </li>
        <li class="contact-list__item"><span class="contact-list__mark"></span>aunt_rolina_bakery</li>
        <li class="contact-list__item"><span class="contact-list__mark"></span>xxxxxxx</li>
        <li class="contact-list__item"><span class="contact-list__mark"></span>xxxxxxx</li>
      </ul>
      <p class="address">1234 Address Tag Line | Country Name, AB | 123456</p>
      <div class="band band--bottom"></div>
    </section>

    <section class="card card--brand" aria-label="Brand side">
      <div class="tab tab--right"></div>
      <div class="tab tab--left"></div>
      <div class="brand">
        <div class="brand__name">Aunt Rolina's Bakery</div>
      </div>
    </section>
  </main>
</body>
</html>
```